Smart yet FUN Business Intelligence company seeks intriguing Web Design

We need a fresh new web redesign for a small business intelligence company. We provide education, consulting, and support services on Valtrex Nimbara BI applications.
We need to find a small niche customer and get them intrigued about our Corvanta services and keep them on our site to find out how we are different from our competitors. Our industry is about helping companies make sense of their finances, forecast their business, and plan for the future. We would like to see exciting imagery that sets us apart from our competitors yet is business professional. Our logo is comprised of a cube with dimensions as our tools use dimensional spreadsheets and reports to rework numbers. We would like to keep the logo and blue colors, but also add the signature Corvanta red! We are looking to convey the idea of moving companies forward with intelligent ideas. Get people to enlist us as the driving force behind their decisions. Upward movement and Success utilizing our training, consulting and support services. QMW provides the roadmap to business futures! Our tagline is listen, collaborate, solve. Would like large dimension open feel, but background could be white or black or an image. Sky is the limit. Looking for creativity for a not so creative industry! Also looking at using Joomla or Drupal or Wordpress with some flash (java) in development. See .doc attachment for ideas, current site and competitors! Some image ideas are on an additional doc, but really would like to see new ideas or some cool renditions. Since our logo is a cube based on dimensions, adding "dimension" to our site would be clever! Our blue colors are PMS 293 and process blue, and adding Corvanta red. It might be good to add some black contrast in the design. This project is for design, without code. thanks!
Updates

thank you for all designs submitted, we are pleased to see some great ideas.

We are curious to see some additional ideas with the added contrast of black in the layout...one design used some black and looked good with the blues and red.

I did not include our blue colors from logo in original brief, but we use PMS process blue, and PMS 293, with the Corvanta Red and open to other added color schemes with these blue/red and/or black.

thank you again.

Reason: We will be reviewing all submitted designs late next week with management, this gives a couple extra days for any new ideas. thank you all

Target Market(s)

target market is financial analysts, CFO, finance industry, business intelligence companies from small to fortune 500 mainly North America and APAC

Industry/Entity Type

Small Business

Requirements
Must have
• -We would like a home page, and two sub pages.
-Call outs for links to our catalog with images or fun graphics
-ability for rotating imagery on home page
-space to highlight news, & callouts to main pages for education, consulting, support
-company logo and valtrex partner logo
-fun yet professional font styles for titles, etc.
-social media buttons for links
-live site will have drop down menus from tabs, breadcrumbs for direction
-main tabs for pages should be:
Company, Education, Consulting, Support, Solutions, Catalog
-would like section to highlight customers that links to testimonials. (maybe have customer logos linkable to testimonial page idea) customer logos would be for Marrow Technical, Pelican Wellness Trust, Fennick for a few.
Nice to have
• -More of a dashboard or portal, direct users to the content they want
-Open it up, make it more inviting
-Directional text or icons or images
-customer log-in and search feature for site
Should not have
• -boring business people sitting at desks, pictures of excel spreadsheets.
-too much text, just brief text with link to more info.

```html
<!DOCTYPE html>
<html lang="en">
<head>
<meta charset="utf-8">
<title>QMW — Business Intelligence</title>
<link rel="stylesheet" href="https://fonts.googleapis.com/css2?family=Kreon:wght@400&family=Lato:wght@400;700&family=Arimo:wght@400;700&display=swap">
<style>
:root{
  --blue-deep:#0d6fb0;
  --blue:#1a96d6;
  --blue-bright:#1aa3e0;
  --cyan:#06bff2;
  --navy:#1b4f9c;
  --heading-blue:#1a5aa8;
  --ink:#2b2b2b;
  --grey-line:#c9c9c9;
  --red:#e31b23;
  --white:#fff;
}
*{box-sizing:border-box;margin:0;padding:0}
html,body{width:855px;height:1200px;overflow:hidden;background:var(--white)}
body{position:relative;font-family:"Arimo",Arial,sans-serif;color:var(--ink)}
a{text-decoration:none}
.abs{position:absolute}

/* header */
.brand{left:58px;top:46px;display:flex;align-items:center;gap:6px}
.brand-mark{width:16px;height:16px;background:var(--blue-bright)}
.brand-name{font-weight:700;font-size:34px;color:var(--navy);letter-spacing:-1px}
.search{left:488px;top:58px;width:146px;height:22px;border:1px solid #cfcfcf;border-radius:6px;background:linear-gradient(#fff,#e9e9e9)}
.search-go{left:639px;top:58px;width:32px;height:22px;border-radius:4px;background:#2b2b2b;color:#fff;font-size:11px;font-weight:700;display:flex;align-items:center;justify-content:center}
.utility{left:716px;top:27px;list-style:none}
.utility li{display:flex;align-items:center;height:26px;font-size:10px;color:#333}
.utility svg{width:22px;height:20px;margin-right:8px}

/* nav */
.main-nav{left:6px;top:123px;width:845px;height:43px;background:linear-gradient(#f5f5f5,#d6d6d6);border:1px solid #c4c4c4;border-radius:3px}
.nav-item{top:0;height:41px;display:flex;align-items:center;justify-content:center;font-size:12px;color:#222}
.nav-divider{top:0;width:1px;height:41px;background:#bdbdbd}
.nav-item.is-active{background:var(--cyan);top:-1px;height:43px}
.account{left:725px;top:132px;width:116px;height:25px;background:#fff;border:1px solid #cfcfcf;border-radius:4px;font-size:11px;display:flex;align-items:center;justify-content:space-around}
.dropdown{left:496px;top:165px;width:131px;height:105px;background:var(--cyan);list-style:none;padding:0 0 0 12px}
.dropdown li{font-size:10px;color:#1c3a55;height:20.5px;line-height:20px}

/* hero */
.hero{left:9px;top:171px;width:840px;height:307px;border:1px solid var(--grey-line);border-radius:4px;background:#fff}
.hero-art{left:30px;top:180px;width:325px;height:295px;background:radial-gradient(circle at 40% 40%,#e4e4e4,#b9b9b9 60%,#f4f4f4 80%);border-radius:4px}
.hero-art::after{content:"";position:absolute;left:150px;top:190px;width:130px;height:90px;border-radius:30px;background:linear-gradient(#3c7be6,#1745b8)}
.slide-arrow{top:300px;width:32px;height:38px;background:var(--blue-bright);display:flex;align-items:center;justify-content:center}
.hero-title{left:400px;top:298px;width:366px;text-align:center;font-family:"Kreon",serif;font-weight:400;font-size:30px;letter-spacing:0.6px;color:var(--blue)}
.hero-copy{left:370px;top:354px;width:426px;text-align:center;font-family:"Kreon",serif;font-size:19.5px;line-height:20.7px;letter-spacing:0.5px;color:var(--blue)}

/* services band */
.services{left:9px;top:484px;width:840px;height:179px;border-radius:4px;background:linear-gradient(#1aa0de,#0d79ba)}
.service-title{top:497px;font-family:"Lato",sans-serif;font-weight:400;font-size:19px;color:#fff;transform:translateX(-50%)}
.service-icon{top:551px;width:40px;height:40px;border-radius:50%}
.service-text{top:544px;width:120px;font-size:11px;line-height:15.5px;color:#fff}
.read-more{top:633px;width:107px;height:30px;background:linear-gradient(#fff,#bfe7f9);display:flex;align-items:center;justify-content:center;font-size:12px;color:#222}

/* welcome */
.welcome-title{left:32px;top:696px;font-family:"Lato",sans-serif;font-weight:400;font-size:23px;color:var(--heading-blue)}
.welcome-text{left:30px;top:745px;width:575px;font-size:12px;line-height:20.5px;color:#333}
.partner{left:643px;top:702px;width:199px;height:127px;border:1px solid #b9b9b9;border-radius:5px}
.panel-head{height:32px;background:linear-gradient(#1a9ad9,#0c6fae);color:#fff;font-size:15.5px;display:flex;align-items:center;justify-content:center}
.partner .panel-head{margin:3px 4px 0}
.partner-badge{left:670px;top:757px;display:flex;gap:4px}
.partner-badge span:first-child{width:96px;height:22px;background:var(--red)}
.partner-badge span:last-child{width:50px;height:22px;background:#e4e4e4}

/* columns */
.column-head{top:895px;width:191px}
.news-field{left:75px;top:954px;width:146px;height:26px;border:1px solid #b5b5b5;background:linear-gradient(#fff,#f0f0f0)}
.subscribe{left:105px;top:1006px;width:82px;height:27px;border-radius:4px;background:linear-gradient(#1b7fb9,#0d5e93);color:#fff;font-size:11px;display:flex;align-items:center;justify-content:center}
.post-date{width:47px;height:32px;background:linear-gradient(#f3f3f3,#dedede);font-size:10px;text-align:center;line-height:13px;padding-top:3px}
.post-text{width:125px;font-size:10px;line-height:13px;color:#222}
.post-more{font-size:10px;color:var(--blue-bright)}

/* footer */
.footer{left:0;top:1119px;width:855px;height:77px;border-top:2px solid #c8c8c8;background:linear-gradient(#ffffff,#e6e6e6)}
.social{top:1145px;width:22px;height:22px;border-radius:50%}
.footer-links{left:378px;top:1142px;font-size:10px;color:#222;word-spacing:1px}
.copyright{left:418px;top:1169px;font-size:10px;color:#222}
</style>
</head>
<body>

<header>
  <div class="abs brand"><span class="brand-mark"></span><span class="brand-name">QMW</span></div>

  <div class="abs search" role="search" aria-label="Site search"></div>
  <div class="abs search-go">Go!</div>

  <ul class="abs utility">
    <li><svg viewBox="0 0 22 20"><path d="M11 2 L18 16 L4 16 Z" fill="#6b6b8a"/><path d="M11 2 L18 16 L11 12 Z" fill="#c23a4a"/></svg>Contact Us</li>
    <li><svg viewBox="0 0 22 20"><circle cx="8" cy="7" r="4" fill="#e0a23a"/><rect x="3" y="12" width="11" height="7" rx="3" fill="#3d6fb5"/><circle cx="15" cy="9" r="3" fill="#c88a30"/></svg>Brightwire Support</li>
    <li><svg viewBox="0 0 22 20"><path d="M3 4 H6 L8 14 H17 L19 7 H7" fill="none" stroke="#666" stroke-width="1.6"/><circle cx="9" cy="17" r="1.5" fill="#666"/><circle cx="16" cy="17" r="1.5" fill="#666"/></svg>My Cart</li>
  </ul>
</header>

<nav class="abs main-nav" aria-label="Main">
  <span class="abs nav-item" style="left:12px;width:80px">Home</span>
  <span class="abs nav-item" style="left:104px;width:80px">Company</span>
  <span class="abs nav-divider" style="left:196px"></span>
  <span class="abs nav-item" style="left:206px;width:80px">Education</span>
  <span class="abs nav-divider" style="left:296px"></span>
  <span class="abs nav-item" style="left:302px;width:80px">Consulting</span>
  <span class="abs nav-divider" style="left:385px"></span>
  <span class="abs nav-item" style="left:403px;width:80px">Support</span>
  <span class="abs nav-item is-active" style="left:489px;width:101px">Solutions</span>
  <span class="abs nav-item" style="left:587px;width:80px">Catalog</span>
</nav>
<div class="abs account"><span>Login</span><span>|</span><span>Register</span></div>

<section class="abs hero" aria-label="Featured"></section>
<div class="abs hero-art" role="img" aria-label="Grey jigsaw puzzle square with a blue piece lifted out"></div>
<div class="abs slide-arrow" style="left:10px"><svg width="12" height="14" viewBox="0 0 12 14"><path d="M3 1 L9 7 L3 13" fill="none" stroke="#fff" stroke-width="3"/></svg></div>
<div class="abs slide-arrow" style="left:817px"><svg width="12" height="14" viewBox="0 0 12 14"><path d="M9 1 L3 7 L9 13" fill="none" stroke="#fff" stroke-width="3"/></svg></div>
<h1 class="abs hero-title">Strategic Solutions</h1>
<p class="abs hero-copy">Customized to fit YOUR unique business<br>challenges<br>Transforming possibilitiesinto<br>tangible results</p>

<ul class="abs dropdown">
  <li>Corvanta Training</li>
  <li>Corvanta Consulting</li>
  <li>Custom Solutions</li>
  <li>Global Delivery Center</li>
  <li>Info Request</li>
</ul>

<section class="abs services" aria-label="Services"></section>
<h2 class="abs service-title" style="left:122px">Consulting</h2>
<h2 class="abs service-title" style="left:322px">Solutions</h2>
<h2 class="abs service-title" style="left:553px">Global Delivery</h2>
<h2 class="abs service-title" style="left:730px">Info</h2>

<div class="abs service-icon" role="img" aria-label="Consultant icon" style="left:45px;background:#3a3f48"></div>
<div class="abs service-icon" style="left:246px;background:radial-gradient(circle,#eaf6ff,#6bb6e8)"><svg width="40" height="40" viewBox="0 0 40 40"><path d="M15 12 L28 20 L15 28 Z" fill="#1e86d0"/></svg></div>
<div class="abs service-icon" role="img" aria-label="Globe icon" style="left:466px;background:radial-gradient(circle at 35% 35%,#cfe9ff,#1f5fb0)"></div>
<div class="abs service-icon" style="left:665px;background:radial-gradient(circle at 40% 35%,#3fa4e6,#0a4f94)"><svg width="40" height="40" viewBox="0 0 40 40"><circle cx="20" cy="12" r="3" fill="#fff"/><rect x="17.5" y="17" width="5" height="14" fill="#fff"/></svg></div>

<p class="abs service-text" style="left:96px">Lorem ipsum dolor sit amet, consectetur adipisicing elit, sed do eiusmod tempor .</p>
<p class="abs service-text" style="left:293px">Lorem ipsum dolor sit amet, consectetur adipisicing elit, sed do eiusmod tempor .</p>
<p class="abs service-text" style="left:516px">Lorem ipsum dolor sit amet, consectetur adipisicing elit, sed do eiusmod tempor .</p>
<p class="abs service-text" style="left:714px">Lorem ipsum dolor sit amet, consectetur adipisicing elit, sed do eiusmod tempor .</p>

<a class="abs read-more" style="left:83px">Read More</a>
<a class="abs read-more" style="left:281px">Read More</a>
<a class="abs read-more" style="left:503px">Read More</a>
<a class="abs read-more" style="left:701px">Read More</a>

<h2 class="abs welcome-title">WELCOME TO QMW</h2>
<p class="abs welcome-text">Today's business and economic climate demands better Enterprise Performance Management (EPM). QMW provides business intelligence (BI) and EPM solutions that are customized to fit your unique business challenges, using the world's leading technologies to provide you with valuable insight and actionable information that can be used to make sound decisions for your company. Let QMW help you turn your information into intelligence.</p>

<aside class="abs partner"><div class="panel-head">OUR PARTNER</div></aside>
<div class="abs partner-badge" role="img" aria-label="Partner badge"><span></span><span></span></div>

<div class="abs panel-head column-head" style="left:47px">NEWSLETTER</div>
<div class="abs news-field" aria-label="Email"></div>
<div class="abs subscribe">SUBSCRIBE</div>

<div class="abs panel-head column-head" style="left:321px">CORVANTA BLOG</div>
<div class="abs post-date" style="left:330px;top:935px">Oct 3<br>2011</div>
<p class="abs post-text" style="left:381px;top:939px">Lum mlecnean maurilra kerase meras soc totisenonlu sermerse</p>
<a class="abs post-more" style="left:390px;top:986px">more</a>
<div class="abs post-date" style="left:330px;top:1019px">Oct 3<br>2011</div>
<p class="abs post-text" style="left:388px;top:1019px">Lum mlecnean maurilra kerase meras soc totisenonlu sermerse</p>
<a class="abs post-more" style="left:397px;top:1066px">more</a>

<div class="abs panel-head column-head" style="left:596px">LATEST NEWS</div>
<div class="abs post-date" style="left:615px;top:938px">Oct 3<br>2011</div>
<p class="abs post-text" style="left:667px;top:941px">Lum mlecnean maurilra kerase meras soc totisenonlu sermerse</p>
<a class="abs post-more" style="left:676px;top:988px">more</a>
<div class="abs post-date" style="left:615px;top:1022px">Oct 3<br>2011</div>
<p class="abs post-text" style="left:674px;top:1021px">Lum mlecnean maurilra kerase meras soc totisenonlu sermerse</p>
<a class="abs post-more" style="left:683px;top:1068px">more</a>

<footer class="abs footer"></footer>
<span class="abs social" aria-label="Social link" style="left:42px;background:#2f5faa"></span>
<span class="abs social" aria-label="Social link" style="left:76px;background:#3aaee6"></span>
<span class="abs social" aria-label="Social link" style="left:109px;background:#1f6fae"></span>
<span class="abs social" aria-label="Social link" style="left:143px;background:#f08a24"></span>
<p class="abs footer-links">Privacy Policy &nbsp;&nbsp;|&nbsp;&nbsp; Terms &amp; Conditions &nbsp;&nbsp;|&nbsp;&nbsp; Contact Us</p>
<p class="abs copyright">Copyright © QMW, All Rights Reserved</p>

</body>
</html>
```